I need a banner ad for a Tee Shirt campaign. I will be promoting "Hats Off Quentin" T-shirts. This will be targeted to College Students and Vortexa Fans. I will not be advertising on ZW so I will not have to worry about Censorship. These are a couple of samples of the type of shirts.

```html
<!DOCTYPE html>
<html lang="en">
<head>
<meta charset="utf-8">
<title>Hats Off Quentin – Tee Campaign</title>
<link rel="stylesheet" href="https://fonts.googleapis.com/css2?family=Poppins:wght@800&family=Anton&family=Arimo:wght@400;700&display=swap">
<style>
  :root {
    --backdrop: #a9a9a9;
    --band-blue: #1f64a0;
    --star-blue: #24508a;
    --star-edge: #4d7fb8;
    --headline-red: #ec1c24;
    --white: #ffffff;
    --texture: #9a9cb6;
    --texture-light: #c4c5d6;
    --shirt: #14161a;
    --footer: #000000;
    --out-now: #1a5c9c;
  }
  * { margin: 0; padding: 0; box-sizing: border-box; }
  html, body { width: 1200px; height: 1200px; overflow: hidden; background: var(--backdrop); }
  .canvas { position: relative; width: 1200px; height: 1200px; background: var(--backdrop); }
  .poster {
    position: absolute; left: 293px; top: 183px; width: 615px; height: 834px;
    background: var(--white); overflow: hidden;
  }
  .top-band { position: absolute; left: 0; top: 0; width: 615px; height: 124px; background: var(--band-blue); }
  .texture-field {
    position: absolute; left: 0; top: 175px; width: 615px; height: 598px;
    background: radial-gradient(ellipse at 50% 40%, var(--texture) 0%, var(--texture) 55%, var(--texture-light) 100%);
  }
  .star-shape { position: absolute; left: 0; top: 0; width: 615px; height: 834px; }
  .shirt {
    position: absolute; background: var(--shirt); border-radius: 26px;
  }
  .shirt-flag { left: 30px; top: 250px; width: 275px; height: 320px; transform: rotate(-4deg); }
  .shirt-banner { left: 325px; top: 430px; width: 260px; height: 320px; transform: rotate(11deg); }
  .headline { position: absolute; left: 0; top: 0; width: 615px; height: 260px; }
  .headline text { font-family: "Poppins", sans-serif; font-weight: 800; }
  .out-now {
    position: absolute; left: 336px; top: 307px; width: 232px; text-align: center;
    font-family: "Anton", sans-serif; font-size: 60px; line-height: 1; color: var(--out-now);
    letter-spacing: 1px;
    -webkit-text-stroke: 2px var(--white);
    paint-order: stroke fill;
  }
  .info { position: absolute; left: 41px; top: 603px; width: 220px; text-align: center; color: var(--white); font-family: "Arimo", sans-serif; }
  .info-title { font-size: 16px; font-weight: 700; letter-spacing: 0.3px; margin-bottom: 18px; }
  .info-body { font-size: 12.2px; line-height: 15.7px; }
  .footer {
    position: absolute; left: 0; top: 773px; width: 615px; height: 61px; background: var(--footer);
    display: flex; align-items: center; justify-content: center;
    color: var(--white); font-family: "Arimo", sans-serif; font-weight: 700; font-size: 28px; letter-spacing: 0.3px;
  }
</style>
</head>
<body>
<div class="canvas">
  <div class="poster">
    <div class="top-band"></div>
    <div class="texture-field" role="img" aria-label="Distressed grey grunge texture background"></div>

    <svg class="star-shape" viewBox="0 0 615 834" aria-hidden="true">
      <polygon points="122,435 209,573 369,545 265,670 341,814 190,753 76,870 88,708 -59,636 99,596"
               fill="var(--star-blue)" stroke="var(--star-edge)" stroke-width="10" stroke-linejoin="miter"/>
      <polygon points="431,221 481,221 481,244 511,244 456,294 401,244 431,244" fill="var(--white)"/>
    </svg>

    <div class="shirt shirt-flag" role="img" aria-label="Black T-shirt printed with a distressed flag and the words Hats Off Quentin"></div>
    <div class="shirt shirt-banner" role="img" aria-label="Black T-shirt printed with Hats Off Quentin between red and blue star stripes"></div>

    <svg class="headline" viewBox="0 0 615 260" aria-label="Hats Off Quentin">
      <g text-anchor="middle" font-size="112">
        <text x="306" y="127" textLength="440" lengthAdjust="spacingAndGlyphs" fill="var(--band-blue)" stroke="var(--band-blue)" stroke-width="30" stroke-linejoin="round">HATS OFF</text>
        <text x="306" y="209" textLength="510" lengthAdjust="spacingAndGlyphs" fill="var(--band-blue)" stroke="var(--band-blue)" stroke-width="30" stroke-linejoin="round">QUENTIN</text>
        <text x="306" y="127" textLength="440" lengthAdjust="spacingAndGlyphs" fill="var(--white)" stroke="var(--white)" stroke-width="16" stroke-linejoin="round">HATS OFF</text>
        <text x="306" y="209" textLength="510" lengthAdjust="spacingAndGlyphs" fill="var(--white)" stroke="var(--white)" stroke-width="16" stroke-linejoin="round">QUENTIN</text>
        <text x="306" y="127" textLength="440" lengthAdjust="spacingAndGlyphs" fill="var(--headline-red)">HATS OFF</text>
        <text x="306" y="209" textLength="510" lengthAdjust="spacingAndGlyphs" fill="var(--headline-red)">QUENTIN</text>
      </g>
    </svg>

    <div class="out-now">OUT NOW</div>

    <div class="info">
      <p class="info-title">TEXT HERE</p>
      <p class="info-body">Lorem Ipsum Dolor Sit<br>Amet Lorem Ipsum Dolor Sit Amet<br>Lorem Ipsum Dolor Sit Amet<br>Lorem Ipsum Dolor Sit Amet Lorem<br>Ipsum Dolor Sit Amet Lorem<br>Ipsum Dolor Sit Amet Lorem Ipsum<br>Dolor Sit Amet.</p>
    </div>

    <div class="footer">www.hatsoffquentin.com</div>
  </div>
</div>
</body>
</html>
```